Lumvex Crating Business Card

Project Overview
We are seeking a modern, minimalist business card that effectively represents our company while making a bold and lasting impression. The design should reflect trust, professionalism, and innovation, reinforcing our expertise in custom plastic manufacturing for warehouse and distribution centers.

Provided Assets & Specifications
Logo: We will provide our official logo for integration into the design.
Design Files: Photoshop (PSD) files for our printing specifications will be supplied.

Card Size & Material:
Dimensions: 3.5" x 2"
Material: 1/8" Radius Plastic Business Cards with 1/8" Rounded Corners
Clear plastic background—the design should strategically incorporate transparency.
Orientation: The card should be designed in landscape format for a sleek and professional presentation.

Design Requirements:
Logo Prominence
The logo must be the focal point of the card.
Space should be used effectively to draw attention to the logo while maintaining a minimalist layout.

Clear Plastic Integration
The transparent background should create the illusion of blank space, enhancing the modern and high-quality feel.
Avoid any frosted effects—we do not want white areas to appear semi-transparent.

Minimalist & Impactful
Clean, structured, and easy to read at a glance.
Focus on sharp contrast to ensure legibility and visibility.
The design should instill confidence and reflect our role as a leading plastics manufacturer.

Color Palette & Contrast
Primary Colors: Blue, Black, White, and Grey
Use bold black or blue for text and key elements to ensure they stand out against the clear plastic.
Avoid light, pastel, or neon colors that may fade into the plastic background.
No frosted or semi-transparent white—we do not want a cloudy effect.

Typography & Information Hierarchy
Bold, modern typography—clear, professional, and highly legible.
The business card should highlight:
Company Logo (Primary Focus)
Full Name & Title
Phone Number
Email
Website

Brand Representation
The card should reflect our expertise in manufacturing high-quality custom plastics for large-scale packaging and distribution businesses.
Our clients rely on us to enhance their brand presence through custom plastic solutions, and our business cards should reinforce that sense of precision and trust.

Final Considerations
Utilize the clear plastic effectively to differentiate our brand from standard business cards.
Maintain a sleek, professional aesthetic while ensuring all text and elements remain legible.
The design should align with our industry, conveying reliability and innovation.
We look forward to seeing a design that captures our brand identity, maximizes the clear plastic medium, and makes a strong, professional impact on our clients.

```html
<!DOCTYPE html>
<html lang="en">
<head>
<meta charset="UTF-8">
<title>Lumvex Crating Business Card</title>
<link href="https://fonts.googleapis.com/css2?family=Montserrat:wght@400;500;700&display=swap" rel="stylesheet">
<style>
  :root {
    --stage: #2b2b2b;
    --card: #141414;
    --card-edge: #202020;
    --blue: #0a8ccc;
    --white: #ffffff;
    --text-soft: #e6e6e6;
    --silver: #c9c9c9;
  }
  * { margin: 0; padding: 0; box-sizing: border-box; }
  html, body {
    width: 1200px; height: 689px; overflow: hidden;
    background: var(--stage);
    font-family: "Montserrat", sans-serif;
  }
  .canvas {
    position: relative; width: 1200px; height: 689px;
    display: flex; align-items: center; justify-content: center; gap: 40px;
  }
  .card {
    position: relative; width: 540px; height: 309px;
    border-radius: 19px; background: var(--card);
    box-shadow: 0 0 0 1px var(--card-edge), 0 18px 40px rgba(0,0,0,.45);
    overflow: hidden;
  }
  .card-front__pattern {
    position: absolute; inset: 0;
    background: linear-gradient(115deg, var(--silver) 0%, #7a7a7a 28%, #2a2a2a 55%, #0c0c0c 100%);
    opacity: .9;
  }
  .card-back { display: flex; align-items: center; }
  .brand {
    width: 285px; display: flex; align-items: center; justify-content: center; gap: 12px;
    padding-left: 20px;
  }
  .brand__mark { width: 22px; height: 22px; background: var(--blue); flex: none; }
  .brand__name {
    color: var(--white); font-weight: 700; font-size: 26px; letter-spacing: .5px;
    white-space: nowrap;
  }
  .divider { width: 2px; height: 176px; background: var(--blue); flex: none; }
  .details { padding-left: 24px; color: var(--text-soft); font-size: 13px; line-height: 1.35; }
  .details__name { color: var(--blue); font-weight: 700; font-size: 25px; letter-spacing: .5px; line-height: 1.1; }
  .details__title { font-weight: 500; font-size: 13.5px; margin-bottom: 12px; color: var(--white); }
  .details__address { margin-bottom: 10px; }
  .contact { list-style: none; }
  .contact li { display: flex; align-items: center; gap: 8px; }
  .contact svg { width: 12px; height: 12px; flex: none; fill: var(--blue); }
</style>
</head>
<body>
<main class="canvas">
  <section class="card card-front">
    <div class="card-front__pattern" role="img" aria-label="Repeating pattern of outlined cubes fading from silver to black"></div>
  </section>

  <section class="card card-back">
    <div class="brand">
      <span class="brand__mark"></span>
      <span class="brand__name">Lumvex Crating</span>
    </div>
    <div class="divider"></div>
    <div class="details">
      <h1 class="details__name">OWEN HARTLEY</h1>
      <p class="details__title">Managing Director</p>
      <p class="details__address">Your address, City<br>State, Zip 1234</p>
      <ul class="contact">
        <li><svg viewBox="0 0 24 24"><path d="M6.6 10.8a15.1 15.1 0 0 0 6.6 6.6l2.2-2.2a1 1 0 0 1 1-.25 11.4 11.4 0 0 0 3.6.57 1 1 0 0 1 1 1V20a1 1 0 0 1-1 1A17 17 0 0 1 3 4a1 1 0 0 1 1-1h3.5a1 1 0 0 1 1 1c0 1.25.2 2.45.57 3.57a1 1 0 0 1-.25 1z"/></svg>123 456 789</li>
        <li><svg viewBox="0 0 24 24"><path d="M2 5h20v14H2z M2 5l10 8 10-8" /></svg>info@yourmail.com</li>
        <li><svg viewBox="0 0 24 24"><circle cx="12" cy="12" r="10"/></svg>www.yourwebsite.com</li>
      </ul>
    </div>
  </section>
</main>
</body>
</html>
```